Website for IT consulting Company

I need a website upgrade, the existing site content is ok, I would also like to add a testimonial page, the site should be something that is easy for us to update content. You use the content from www.velmarketa.com as an example. I will also post update logo and artwork. I also need a contact form with some type of validation or captcha.

Please omit Address maps

Target Market(s)

small business, service oriented companies. We provide IT Consulting, support and mangement

Industry/Entity Type

Information Technology

Coding

Coded - Design and coding required

Number of Pages Required

1 page

Font styles to use
Serif
Sans Serif

Requirements
Must have
• Contain logo attached, and content from existing web site www.velmarketa.com.
• Also need to update content easily, and be movable to different platforms.
• There is a catch phrase
• "Let us worry about your technology…” “ so you don’t have to!”
• Should be included.
Nice to have
• Testimonial page, Project page where we can post new and past projects and pictures
Should not have
• none

```html
<!DOCTYPE html>
<html lang="en">
<head>
<meta charset="utf-8">
<title>Velmarketa – IT Solutions</title>
<link href="https://fonts.googleapis.com/css2?family=Roboto:wght@300;400;500;700&display=swap" rel="stylesheet">
<style>
:root{
  --orange:#f28a2a;
  --orange-dark:#e0741b;
  --blue:#1f97d6;
  --blue-dark:#137fbf;
  --ink:#222;
  --text:#555;
  --grey-bg:#f3f3f3;
  --field:#f1f1f1;
  --footer:#1c1d22;
  --footer-text:#b9bcc4;
  --white:#fff;
}
*{margin:0;padding:0;box-sizing:border-box}
html,body{width:1200px;height:2866px;overflow:hidden;background:var(--white)}
body{font-family:"Roboto",Arial,sans-serif;color:var(--text);position:relative}
.abs{position:absolute}

/* header */
.site-header{left:0;top:0;width:1200px;height:56px;background:var(--white);box-shadow:0 1px 3px rgba(0,0,0,.08);z-index:3}
.brand{left:90px;top:14px;display:flex;align-items:center;gap:8px;font-weight:700;font-size:20px;color:var(--blue);letter-spacing:1px}
.brand-mark{width:18px;height:18px;background:var(--blue);border-radius:3px}
.main-nav{left:530px;top:0;height:56px;display:flex}
.main-nav a{display:block;padding:22px 14px 0;height:56px;font-size:12.5px;font-weight:400;color:#333;text-decoration:none;text-transform:uppercase}
.main-nav a.active{color:var(--orange);border-top:3px solid var(--orange);padding-top:19px}

/* hero */
.hero{left:0;top:56px;width:1200px;height:586px;background:linear-gradient(100deg,#5d5f62 0%,#8b8680 30%,#b3a79d 55%,#6e6a68 80%,#4a4b4e 100%)}
.hero-shade{left:0;top:56px;width:1200px;height:586px;background:rgba(0,0,0,.18)}
.hero-title{left:0;top:326px;width:1200px;text-align:center;color:var(--white);font-size:37px;line-height:35px;font-weight:400;text-transform:uppercase}
.hero-sub{left:0;top:406px;width:1200px;text-align:center;color:var(--white);font-size:16px}
.hero-prev,.hero-next{top:369px;color:var(--white);font-size:11px;font-weight:500}
.hero-prev{left:34px}.hero-next{left:1110px}
.scroll-down{left:581px;top:623px;width:38px;height:38px;border-radius:50%;background:var(--white);box-shadow:0 1px 4px rgba(0,0,0,.25);z-index:2}

/* intro */
.section-title{left:0;width:1200px;text-align:center;color:var(--ink);font-size:27px;font-weight:400;text-transform:uppercase}
.title-rule{left:585px;width:30px;height:2px;background:#ccc}
.intro-text{left:180px;top:772px;width:840px;text-align:center;font-size:13.5px;line-height:21px;color:#444}
.btn{background:var(--orange);color:var(--white);border-radius:20px;font-size:11px;font-weight:500;text-transform:uppercase;display:flex;align-items:center;justify-content:center;gap:8px}
.learn-more{left:537px;top:873px;width:128px;height:38px}

/* services */
.services{left:0;top:986px;width:1200px;height:457px;background:var(--grey-bg)}
.photo-circle{border-radius:50%}
.photo-large{left:170px;top:1055px;width:298px;height:298px;background:linear-gradient(160deg,#d8d4cf,#9c8f84 60%,#5a524d)}
.photo-small{left:-94px;top:1163px;width:300px;height:300px;background:linear-gradient(150deg,#d6ccc4,#a78d7b 55%,#6b5a52);border:9px solid var(--white)}
.service{left:548px;width:520px}
.service-icon{position:absolute;left:0;top:0;width:44px;height:40px}
.service h3{margin-left:62px;font-size:14px;font-weight:400;color:var(--ink);text-transform:uppercase;margin-bottom:6px}
.service p{margin-left:62px;width:450px;font-size:11.5px;line-height:19px;color:#555}

/* flexible */
.flex-band{left:0;top:1443px;width:1200px;height:413px;background:linear-gradient(90deg,var(--orange),var(--orange-dark))}
.flex-title{left:90px;top:1561px;width:520px;color:var(--white);font-size:28px;line-height:28px;text-transform:uppercase;font-weight:400}
.flex-rule{left:90px;top:1622px;width:24px;height:2px;background:var(--white)}
.flex-text{left:90px;top:1638px;width:545px;color:var(--white);font-size:11.5px;line-height:21px}
.flex-tag{left:84px;top:1734px;color:var(--white);font-size:14px;text-transform:uppercase}
.flex-photo{left:688px;top:1502px;width:422px;height:308px;background:linear-gradient(120deg,#f4f4f4,#dcd8d4 50%,#8d8883);border:3px solid var(--white)}

/* contact */
.field{background:var(--field);font-size:11px;color:#777;padding:14px 18px}
.captcha{left:204px;top:2188px;width:268px;height:67px;background:#f9f9f9;border:1px solid #d3d3d3;border-radius:3px;box-shadow:0 0 3px rgba(0,0,0,.08)}
.captcha span{position:absolute;left:46px;top:25px;font-size:12px;color:#222}
.captcha .badge{position:absolute;left:216px;top:12px;width:28px;height:28px;border-radius:4px;background:#c9d5ec}
.captcha small{position:absolute;left:206px;top:44px;font-size:8px;color:#666}
.send{left:795px;top:2203px;width:195px;height:41px;font-size:12px}

/* slogan */
.slogan{left:0;top:2339px;width:1200px;height:178px;background:linear-gradient(90deg,var(--blue),var(--blue-dark))}
.slogan-text{left:0;top:2402px;width:1200px;text-align:center;color:var(--white);font-size:32px;line-height:33px;text-transform:uppercase}

/* footer */
.site-footer{left:0;top:2517px;width:1200px;height:349px;background:var(--footer)}
.footer-brand{left:125px;top:2660px;display:flex;align-items:center;gap:10px;color:var(--white);font-size:27px;font-weight:700;letter-spacing:1px}
.footer-brand i{width:22px;height:22px;background:var(--white);border-radius:3px;display:block}
.copyright{left:80px;top:2718px;width:300px;text-align:center;font-size:12px;line-height:20px;color:var(--footer-text)}
.footer-heading{font-size:14px;font-weight:500;color:var(--white);text-transform:uppercase}
.footer-heading::after{content:"";display:block;width:22px;height:2px;background:var(--white);margin-top:6px}
.footer-list{list-style:none}
.footer-list li{font-size:12px;color:var(--footer-text);height:25px;display:flex;align-items:center;gap:12px}
.footer-list li::before{content:"→";color:#777;font-size:12px}
.to-top{left:1137px;top:2794px;width:38px;height:38px;border-radius:50%;background:var(--orange)}
</style>
</head>
<body>

<header class="site-header abs">
  <div class="brand abs"><span class="brand-mark"></span>VELMARKETA</div>
  <nav class="main-nav abs">
    <a class="active">Home</a><a>Support</a><a>Projects</a><a>Clients</a><a>Testimonials</a><a>Careers</a><a>Contact</a>
  </nav>
</header>

<div class="hero abs" role="img" aria-label="Photo of a smiling team of young professionals gathered around a laptop"></div>
<div class="hero-shade abs"></div>
<h1 class="hero-title abs">IT Solutions that<br>work for your business</h1>
<p class="hero-sub abs">A full service technology company.</p>
<span class="hero-prev abs">PREVIOUS</span>
<span class="hero-next abs">NEXT</span>
<div class="scroll-down abs">
  <svg width="38" height="38" viewBox="0 0 38 38"><path d="M15 17l4 4 4-4" fill="none" stroke="#333" stroke-width="1.8"/></svg>
</div>

<h2 class="section-title abs" style="top:718px">What is&nbsp; outsourcing ?</h2>
<div class="title-rule abs" style="top:760px"></div>
<p class="intro-text abs">Outsourcing is subcontracting a process, such as product design or manufacturing, to a third-party company.[1]<br>The decision to outsource is often made in the interest of lowering firm costs, redirecting or conserving energy directed at the competencies of a particular business, or to make more efficient use of land, labor, capital, (information) technology and resources. Outsourcing became part of the business lexicon during the 1980s.</p>
<div class="btn learn-more abs"><span>→</span>Learn more</div>

<section class="services abs"></section>
<div class="photo-circle photo-large abs" role="img" aria-label="Photo of colleagues working together at a table with laptops"></div>
<div class="photo-circle photo-small abs" role="img" aria-label="Photo of a woman working on a laptop"></div>

<div class="service abs" style="top:1072px">
  <svg class="service-icon" viewBox="0 0 44 40"><circle cx="14" cy="14" r="10" fill="#2aa6df"/><circle cx="14" cy="14" r="4" fill="#fff"/><circle cx="31" cy="22" r="6" fill="#f26b3a"/><circle cx="22" cy="34" r="5" fill="#3bc7a8"/></svg>
  <h3>Managed IT Solutions</h3>
  <p>Our staff will design, service, administer and maintain your IT needs. We are well versed on all major operating system, and network appliances</p>
</div>
<div class="service abs" style="top:1170px">
  <svg class="service-icon" viewBox="0 0 44 40"><rect x="4" y="4" width="36" height="24" rx="2" fill="#f28a2a"/><rect x="8" y="8" width="28" height="16" fill="#fff"/><rect x="11" y="12" width="14" height="3" fill="#2aa6df"/><rect x="18" y="28" width="8" height="6" fill="#999"/><rect x="12" y="34" width="20" height="3" fill="#777"/></svg>
  <h3>Remote Diagnostic and Support</h3>
  <p>Do you need a quick solution to a technical problem? With our live remote-assistance tool, a member of our support team can view your desktop and share control of your mouse and keyboard to get you on your way to a solution.</p>
</div>
<div class="service abs" style="top:1287px">
  <svg class="service-icon" viewBox="0 0 44 40"><rect x="13" y="4" width="18" height="32" rx="9" fill="#d9dde2"/><line x1="22" y1="4" x2="22" y2="16" stroke="#888" stroke-width="1.5"/><line x1="13" y1="16" x2="31" y2="16" stroke="#888" stroke-width="1.5"/></svg>
  <h3>IT Infrastructure Design and Installation</h3>
  <p>Do you have more than one site? Do you need remote access? We can design and implement LANS/WANS and VPN's.&nbsp; Make your important data available to you wherever you are.</p>
</div>

<section class="flex-band abs"></section>
<h2 class="flex-title abs">Flexible solutions for your business needs</h2>
<div class="flex-rule abs"></div>
<p class="flex-text abs">Velmarketa is a technology solution provider based in Corvale Bay. Our goal is to make technology a non-issue for individuals and small to medium size businesses ranging from 5 to 150 Users. Velmarketa has the experience, the tools, high-level technology solutions and training to power your business and your work force. We understand that all business's have one goal in common!</p>
<p class="flex-tag abs">Velmarketa: a return on investment</p>
<div class="flex-photo abs" role="img" aria-label="Photo of a smiling woman working at a desktop computer"></div>

<h2 class="section-title abs" style="top:1936px">Contact us</h2>
<div class="title-rule abs" style="top:1976px"></div>
<div class="field abs" style="left:206px;top:1999px;width:260px;height:42px">Name*</div>
<div class="field abs" style="left:470px;top:1999px;width:258px;height:42px">Email*</div>
<div class="field abs" style="left:734px;top:1999px;width:258px;height:42px">Phone*</div>
<div class="field abs" style="left:206px;top:2049px;width:786px;height:126px">Message*</div>
<div class="captcha abs">
  <svg class="abs" style="left:12px;top:20px" width="28" height="24" viewBox="0 0 28 24"><path d="M3 12l8 8L25 4" fill="none" stroke="#1a9e42" stroke-width="4"/></svg>
  <span>I'm not a robot</span>
  <div class="badge"></div>
  <small>Privacy - Terms</small>
</div>
<div class="btn send abs"><span>→</span>Send message</div>

<section class="slogan abs"></section>
<p class="slogan-text abs">Let us worry about your technology<br>“ so you don’t have to!”</p>

<footer class="site-footer abs"></footer>
<div class="footer-brand abs"><i></i>VELMARKETA</div>
<p class="copyright abs">Copyright © 2017 - Velmarketa Group, Inc -<br>All rights reserved</p>

<div class="abs" style="left:505px;top:2602px"><h4 class="footer-heading">IT Support Solutions</h4></div>
<ul class="footer-list abs" style="left:505px;top:2640px">
  <li>Network Administration</li><li>Desktop support</li><li>Telecommunications</li><li>Disaster recovery</li><li>Audio/video Multimedia</li><li>Web design</li>
</ul>
<ul class="footer-list abs" style="left:714px;top:2640px">
  <li>Network cabling</li><li>Wireless Networks</li><li>Antivirus solutions</li><li>Network security</li>
</ul>
<div class="abs" style="left:932px;top:2602px"><h4 class="footer-heading" style="text-transform:none">Useful Links</h4></div>
<ul class="footer-list abs" style="left:932px;top:2640px">
  <li>Home</li><li>Support</li><li>Projects</li><li>Clients</li><li>Testimonials</li><li>Careers</li><li>Contact</li>
</ul>
<div class="to-top abs">
  <svg width="38" height="38" viewBox="0 0 38 38"><path d="M14 21l5-5 5 5" fill="none" stroke="#fff" stroke-width="2"/></svg>
</div>

</body>
</html>
```